BrookVale Collision Repair Web Site

Create a web site that will inform my potential customers about the services I provide. We are a Automotive Collision repair business that uses the latest state of the art equipment, computerized paint matching highly trained technicians, have over 30 years experience. We work with all all insurance programs. Our Moto is "Fixed Right, The First Time, Every Time". BrookVale, The trusted pick in collision repair.

Target Market(s)

People that have been in a auto collision, needs windshield replaced, people that drive 10 year or newer cars

Industry/Entity Type

Automotive

Coding

Coded - Design and coding required

Number of Pages Required

4 page

Font styles to use
Sans Serif

Requirements
Must have
• Logo, Place for Phone number, I need to be able to put the code in so I can use a tracking phone number
• site needs to be mobile ready or adaptive
• May want to have a photo of a high end car
• here is a web site for example with the pages that I want
• https://www.pondlyautobody.example/online-repair-estimate,
• https://www.pondlyautobody.example/schedule-appointment
• https://www.pondlyautobody.example/collision-repair/auto-body-repair
• https://www.pondlyautobody.example/contact
Nice to have
• Be great if the Car in the log could have the front damaged then have it fix in a animation. Not sure if could be done here

```html
<!DOCTYPE html>
<html lang="en">
<head>
<meta charset="utf-8">
<title>BrookVale Collision Repair</title>
<link href="https://fonts.googleapis.com/css2?family=Open+Sans:wght@300;400;600;700&display=swap" rel="stylesheet">
<style>
:root{
  --green:#8dc63f;
  --green-dark:#7ab52f;
  --blue:#1b56a6;
  --blue-field:#2a66b8;
  --dark:#1b1b1b;
  --text:#555;
  --light:#ececec;
  --white:#fff;
}
*{box-sizing:border-box;margin:0;padding:0}
html,body{width:1200px;height:4423px;overflow:hidden}
body{position:relative;font-family:"Open Sans",Arial,sans-serif;color:var(--text);background:var(--white)}
.abs{position:absolute}
.section{position:absolute;left:0;width:1200px;overflow:hidden}
.photo{position:absolute;inset:0}
.btn{position:absolute;background:var(--green);color:var(--white);font-size:17px;display:flex;align-items:center;justify-content:center;text-transform:uppercase;letter-spacing:.5px;text-decoration:none}
.heading{position:absolute;left:0;width:1200px;text-align:center;color:var(--green);font-size:40px;font-weight:400;letter-spacing:1px;line-height:54px}
.heading-rule{position:absolute;height:2px;background:rgba(255,255,255,.35)}
.lead{position:absolute;left:220px;width:760px;text-align:center;font-size:14.5px;line-height:26px}

/* hero */
.hero{top:0;height:678px}
.hero .photo{background:linear-gradient(100deg,#3b3734 0%,#6b6560 40%,#9c8f84 70%,#5e4f44 100%)}
.hero .shade{position:absolute;inset:0;background:rgba(0,0,0,.25)}
.nav{position:absolute;top:46px;left:280px;width:625px;height:40px;border-bottom:3px solid var(--green)}
.nav a{position:absolute;top:0;color:var(--white);font-size:15px;text-decoration:none;text-transform:uppercase;transform:translateX(-50%)}
.nav a.active{color:var(--green)}
.brand{position:absolute;top:232px;left:0;width:1200px;text-align:center;color:var(--blue);font-size:52px;font-weight:700;letter-spacing:1px}
.tagline{position:absolute;top:395px;left:0;width:1200px;text-align:center;color:var(--white);font-size:40px;font-weight:400;letter-spacing:.5px}

/* estimate */
.estimate{position:absolute;top:566px;left:77px;width:1043px;height:224px;background:var(--blue)}
.estimate-title{position:absolute;top:22px;left:0;width:902px;text-align:center;color:var(--green);font-size:17px;font-weight:700;text-transform:uppercase}
.field{position:absolute;height:40px;border:1px solid rgba(255,255,255,.6);background:var(--blue-field);color:var(--white);font-size:13px;padding:0 12px;display:flex;align-items:center;justify-content:space-between}
.field.select::after{content:"";border:5px solid transparent;border-top:6px solid var(--white);margin-top:5px}
.insurance{position:absolute;left:557px;top:128px;color:var(--white);font-size:13px}
.radios{position:absolute;left:670px;top:156px;color:var(--white);font-size:13px;display:flex;gap:14px;align-items:center}
.radio{display:inline-flex;align-items:center;gap:6px}
.dot{width:13px;height:13px;border-radius:50%;background:var(--white);display:inline-block;border:3px solid var(--white)}
.dot.on{background:var(--blue)}
.continue{position:absolute;top:0;right:0;width:141px;height:224px;background:var(--green);color:var(--white);font-size:17px;display:flex;align-items:center;justify-content:center;text-transform:uppercase}

/* welcome */
.welcome{top:790px;height:551px}
.welcome-photo{position:absolute;left:133px;top:124px;width:362px;height:324px;background:linear-gradient(135deg,#5a6f86,#b33a3a 55%,#3a3a3a)}
.welcome-kicker{position:absolute;left:546px;top:62px;font-size:19px;color:#333;letter-spacing:1px;text-transform:uppercase}
.welcome-brand{position:absolute;left:540px;top:96px;color:var(--blue);font-size:34px;font-weight:700}
.welcome-text{position:absolute;left:540px;top:170px;width:585px;font-size:13.4px;line-height:27px;color:#777}

/* services */
.services{top:1341px;height:619px}
.services .photo{background:linear-gradient(120deg,#1a1a1a,#3d3d3d 45%,#2a2a2a 70%,#4a3a30)}
.services .lead{top:140px;color:var(--white)}
.service{position:absolute;top:222px;width:240px;text-align:center;color:var(--white);transform:translateX(-50%)}
.service-icon{width:112px;height:112px;margin:0 auto;border-radius:50%;border:4px solid var(--green);background:var(--white);display:flex;align-items:center;justify-content:center}
.service-icon span{width:76px;height:76px;border-radius:50%;background:var(--green-dark);display:block}
.service h3{margin-top:30px;font-size:17px;font-weight:400;text-transform:uppercase}
.service p{margin-top:12px;font-size:13px;line-height:24px}

/* what we do */
.whatwedo{top:1960px;height:643px}
.whatwedo .heading-rule{background:#bbb}
.whatwedo .lead{top:134px;color:#777}
.work-card{position:absolute;top:222px;width:510px;height:303px;overflow:hidden}
.work-card .photo{background:linear-gradient(135deg,#2b2b2b,#6e2a2a 60%,#3a3a3a)}
.work-card.paint .photo{background:linear-gradient(135deg,#3a3a3a,#b0235a 55%,#444)}
.work-card .frame{position:absolute;inset:12px;border:1px solid rgba(255,255,255,.5)}
.work-card h3{position:absolute;top:80px;width:100%;text-align:center;color:var(--white);font-size:17px;font-weight:400;text-transform:uppercase}
.work-card p{position:absolute;top:122px;left:70px;width:370px;text-align:center;color:var(--white);font-size:13px;line-height:24px}

/* guarantee */
.guarantee{top:2603px;height:330px;background:var(--light)}
.guarantee h2{position:absolute;left:82px;top:62px;color:var(--green);font-size:38px;font-weight:400;letter-spacing:1.5px;text-transform:uppercase}
.guarantee p{position:absolute;left:85px;top:118px;width:780px;font-size:19px;line-height:33px;color:#666}

/* insurance band */
.band{top:2933px;height:157px;background:var(--green)}
.band h2{position:absolute;left:82px;top:52px;color:var(--white);font-size:38px;font-weight:400}
.band .btn{background:var(--white);color:var(--green);left:840px;top:44px;width:283px;height:68px}

/* testimonials */
.testimonials{top:3090px;height:409px}
.testimonials .photo{background:linear-gradient(120deg,#151515,#3a3a3a 50%,#262626)}
.testimonials .heading-rule{background:rgba(255,255,255,.5)}
.avatar{position:absolute;left:106px;top:158px;width:142px;height:142px;border-radius:50%;border:5px solid var(--white);background:linear-gradient(160deg,#d9c3ad,#8a5a3c)}
.quote-mark{position:absolute;left:252px;top:148px;color:var(--green);font-size:60px;font-weight:700;line-height:1}
.quote{position:absolute;left:295px;top:152px;width:810px;color:var(--white);font-size:14.5px;line-height:35px}
.client{position:absolute;left:295px;top:298px;color:var(--green);font-size:14px;font-weight:600;text-transform:uppercase}
.dots{position:absolute;left:518px;top:340px;display:flex;gap:20px}
.dots i{display:block;width:42px;height:5px;background:var(--white)}
.dots i.on{background:var(--green)}

/* partners */
.partners{top:3499px;height:304px}
.partner{position:absolute;top:62px;width:180px;height:139px;border:1px solid #ddd;display:flex;align-items:center;justify-content:center}
.partner span{width:110px;height:68px;border:2px solid #bbb;border-radius:8px;display:block}
.partner.round span{width:92px;height:92px;border-radius:50%}

/* contact */
.contact{top:3803px;height:560px}
.contact .photo{background:linear-gradient(120deg,#1d1d1d,#3b3b3b 50%,#252525)}
.contact h2{position:absolute;left:97px;top:68px;color:var(--green);font-size:38px;font-weight:400;text-transform:uppercase;letter-spacing:1px}
.contact h3{position:absolute;left:97px;top:148px;color:var(--white);font-size:31px;font-weight:300;text-transform:uppercase}
.address{position:absolute;left:97px;top:212px;color:var(--white);font-size:14.5px;line-height:24px;width:290px}
.phone{position:absolute;left:97px;color:var(--green);font-size:17px}
.phone b{font-weight:400;color:var(--white)}
.input{position:absolute;left:634px;width:466px;height:50px;border:1px solid rgba(255,255,255,.7);color:var(--white);font-size:14px;padding:12px 14px}
.input.message{height:148px}

.footer{top:4363px;height:60px;background:var(--green);color:var(--white);font-size:13px;display:flex;align-items:center;justify-content:center}
</style>
</head>
<body>

<header class="section hero">
  <div class="photo" role="img" aria-label="Smiling driver at the wheel of a car"></div>
  <div class="shade"></div>
  <nav class="nav">
    <a class="active" href="#" style="left:38px">Home</a>
    <a href="#" style="left:150px">About</a>
    <a href="#" style="left:277px">Services</a>
    <a href="#" style="left:433px">Appointment</a>
    <a href="#" style="left:584px">Contact</a>
  </nav>
  <div class="brand">BrookVale Collision Repair</div>
  <h1 class="tagline">FIX RIGHT, THE FIRST TIME, EVERY TIME</h1>
</header>

<form class="estimate">
  <div class="estimate-title">Online Repair Astimet</div>
  <div class="field select" style="left:53px;top:77px;width:156px">Services*</div>
  <div class="field select" style="left:221px;top:77px;width:156px">Year*</div>
  <div class="field select" style="left:389px;top:77px;width:156px">Make*</div>
  <div class="field select" style="left:557px;top:77px;width:156px">Model*</div>
  <div class="field select" style="left:725px;top:77px;width:147px">Body Style*</div>
  <div class="field" style="left:53px;top:130px;width:156px">VIP</div>
  <div class="field select" style="left:221px;top:130px;width:156px">Type of Service</div>
  <div class="field" style="left:389px;top:130px;width:156px">Description</div>
  <div class="insurance">Will an insurance claim be submitted for damages?</div>
  <div class="radios">
    <span class="radio"><i class="dot on"></i>Yes</span>
    <span class="radio"><i class="dot"></i>No</span>
  </div>
  <div class="continue">Continue</div>
</form>

<section class="section welcome">
  <div class="welcome-photo" role="img" aria-label="Technician in red gloves repairing a car headlight"></div>
  <div class="welcome-kicker">Wel come to</div>
  <div class="welcome-brand">BrookVale Collision Repair</div>
  <p class="welcome-text">Lorem Ipsum is simply dummy text of the printing and typesetting industry. Lorem Ipsum has been the industry's standard dummy text ever since the 1500s, when an unknown printer took a galley of type and scrambled it to make a type specimen book. It has survived not only five centuries, but also the leap into electronic typesetting, remaining essentially unchanged. It was popularised in the 1960s with the release of Markwell sheets containing Lorem Ipsum passages, and more recently with desktop publishing software like Quillset Layout including versions of Lorem Ipsum. It is a long established fact that a reader will be distracted by the readable content of a page when looking at its layout. The point of using Lorem Ipsum is that it has a more-or-less normal distribution of letters, as opposed to using 'Content here, content here', making it look like readable English.</p>
</section>

<section class="section services">
  <div class="photo" role="img" aria-label="Mechanic's hands holding a wrench, darkened"></div>
  <div class="heading-rule" style="left:280px;top:85px;width:160px"></div>
  <h2 class="heading" style="top:58px">OUR SERVICES</h2>
  <div class="heading-rule" style="left:760px;top:85px;width:160px"></div>
  <p class="lead">Lorem Ipsum is simply dummy text of the printing and typesetting industry. Lorem Ipsum has been the industry's standard dummy text ever since the 1500s</p>
  <div class="service" style="left:209px"><div class="service-icon"><span role="img" aria-label="Fender repair icon"></span></div><h3>Fender Repair</h3><p>Lorem Ipsum is simply dummy text of the printing and typesetting dummy text...</p></div>
  <div class="service" style="left:463px"><div class="service-icon"><span role="img" aria-label="Bumper repair icon"></span></div><h3>Bumper Repair</h3><p>Lorem Ipsum is simply dummy text of the printing and typesetting dummy text...</p></div>
  <div class="service" style="left:716px"><div class="service-icon"><span role="img" aria-label="Auto dent removal icon"></span></div><h3>Auto Dent Removal</h3><p>Lorem Ipsum is simply dummy text of the printing and typesetting dummy text...</p></div>
  <div class="service" style="left:967px"><div class="service-icon"><span role="img" aria-label="Hail damage repair icon"></span></div><h3>Hail Damage Repair</h3><p>Lorem Ipsum is simply dummy text of the printing and typesetting dummy text...</p></div>
  <a class="btn" style="left:513px;top:507px;width:171px;height:48px">Show All</a>
</section>

<section class="section whatwedo">
  <div class="heading-rule" style="left:260px;top:85px;width:195px"></div>
  <h2 class="heading" style="top:58px">WHAT WE DO</h2>
  <div class="heading-rule" style="left:745px;top:85px;width:195px"></div>
  <p class="lead">Lorem Ipsum is simply dummy text of the printing and typesetting industry. Lorem Ipsum has been the industry's standard dummy text ever since the 1500s</p>
  <div class="work-card" style="left:80px">
    <div class="photo" role="img" aria-label="Technician working on a car body"></div>
    <div class="frame"></div>
    <h3>Art Equipment</h3>
    <p>Lorem Ipsum is simply dummy text of the printing and typesetting Lorem Ipsum has been the industry's Lorem Ipsum is simply dummy text of the printing and typesetting Lorem Ipsum has been the industry's ...</p>
  </div>
  <div class="work-card paint" style="left:613px">
    <div class="photo" role="img" aria-label="Pink sports car in a paint shop"></div>
    <div class="frame"></div>
    <h3>Computerized Paint</h3>
    <p>Lorem Ipsum is simply dummy text of the printing and typesetting Lorem Ipsum has been the industry's Lorem Ipsum is simply dummy text of the printing and typesetting Lorem Ipsum has been the industry's ...</p>
  </div>
  <a class="btn" style="left:513px;top:560px;width:171px;height:48px">Show All</a>
</section>

<section class="section guarantee">
  <h2>Lifetime Guarantee</h2>
  <p>We proudly stand behind our repair work for as long as you own your vehicle. Learn more about our Lifetime Guarantee.</p>
  <a class="btn" style="left:85px;top:203px;width:175px;height:62px">Guarantee</a>
  <svg class="abs" style="left:935px;top:54px" width="176" height="176" viewBox="0 0 176 176" aria-hidden="true">
    <circle cx="88" cy="88" r="86" fill="#b8902e"/>
    <circle cx="88" cy="88" r="66" fill="#2a2a2a"/>
  </svg>
</section>

<section class="section band">
  <h2>We work with all insurance programs.</h2>
  <a class="btn">Schedule Appointment</a>
</section>

<section class="section testimonials">
  <div class="photo" role="img" aria-label="Workshop scene, darkened"></div>
  <div class="heading-rule" style="left:170px;top:87px;width:175px"></div>
  <h2 class="heading" style="top:60px">WHAT OUR CLIENT SAY</h2>
  <div class="heading-rule" style="left:855px;top:87px;width:175px"></div>
  <div class="avatar" role="img" aria-label="Client portrait"></div>
  <div class="quote-mark">&ldquo;</div>
  <p class="quote">Lorem ipsum dolor sit amet, consectetur adipiscing elit. Aenean feugiat dictum lacusLorem ipsum Lorem ipsum dolor sit amet, consectetur adipiscing elit. Aenean feugiat dictum lacusLorem ipsum Lorem ipsum dolor sit amet, consectetur adipiscing elit. Aenean feugiat dictum lacusLorem ipsum Lorem ipsum dolor sit amet, consectetur adipiscing elit. Aenean feugiat dictum lacusLorem ipsum</p>
  <div class="client">Client Name</div>
  <div class="dots"><i></i><i class="on"></i><i></i></div>
</section>

<section class="section partners">
  <div class="partner round" style="left:80px"><span></span></div>
  <div class="partner" style="left:295px"><span></span></div>
  <div class="partner" style="left:510px"><span></span></div>
  <div class="partner" style="left:725px"><span></span></div>
  <div class="partner" style="left:940px"><span></span></div>
</section>

<section class="section contact">
  <div class="photo" role="img" aria-label="Car interior, darkened"></div>
  <h2>Get Started</h2>
  <h3>BrookVale Collision Repair</h3>
  <p class="address">Address, lorem ipsum dummy text for lorem ipsum dolar amet lorem.</p>
  <div class="phone" style="top:292px">Tel: +(91)023 555 0147 <b>FREE</b></div>
  <div class="phone" style="top:325px">Fax: +(91) 123 555 0198</div>
  <a class="btn" style="left:97px;top:392px;width:207px;height:50px">Get Direction</a>
  <div class="input" style="top:68px">Name*</div>
  <div class="input" style="top:133px">Email*</div>
  <div class="input" style="top:198px">Subject*</div>
  <div class="input message" style="top:265px">Message*</div>
  <a class="btn" style="left:899px;top:433px;width:201px;height:56px">Submit</a>
</section>

<footer class="section footer">&copy; BROOKVALE COLLISION REPAIR 2016, All rights reserved.</footer>

</body>
</html>
```